Design our letter, business card, powerpoint and more

We have a logo and want a design for our business use. Letters (word template), business card (for printing) powerpoint presentation (template) and more.

```html
<!DOCTYPE html>
<html lang="en">
<head>
<meta charset="utf-8">
<title>Nordverk Stationery</title>
<link rel="stylesheet" href="https://fonts.googleapis.com/css2?family=Montserrat:wght@400;500&family=Open+Sans:wght@600;700&display=swap">
<style>
:root{
  --bg:#e9eaec;
  --paper:#ffffff;
  --brand-blue:#8faad9;
  --name-blue:#7f9bd3;
  --grey-text:#8a8687;
  --body-text:#9a9698;
  --mark-grey:#a09b9c;
  --dash:#b9b9bd;
  --icon:#8faad9;
}
*{box-sizing:border-box;margin:0;padding:0}
html,body{width:1200px;height:953px;overflow:hidden;background:var(--bg)}
body{position:relative;font-family:'Montserrat',sans-serif;color:var(--grey-text)}
.sheet{position:absolute;background:var(--paper);box-shadow:0 2px 6px rgba(0,0,0,.18)}
.abs{position:absolute}

/* Letterhead */
.letter{left:78px;top:61px;width:588px;height:832px}
.letter .wordmark{left:93px;top:56px;font-family:'Open Sans',sans-serif;font-weight:700;font-size:31px;color:var(--mark-grey);letter-spacing:.5px}
.contact-list{list-style:none}
.contact-list li{display:flex;align-items:center;gap:4px;white-space:nowrap}
.contact-list svg{width:9px;height:9px;flex:none}
.letter .contact-list{left:454px;top:48px;font-size:9.5px;line-height:14.3px}
.dash-rule{left:28px;top:119px;width:533px;border-top:1px dashed var(--dash)}
.recipient{left:34px;top:190px;font-size:11px;line-height:18.5px}
.recipient .name{font-size:14.5px;font-weight:500;color:var(--name-blue);line-height:20px;margin-bottom:1px}
.recipient .addr{line-height:14px;margin-top:2px}
.date{right:32px;top:261px;font-family:'Open Sans',sans-serif;font-weight:600;font-size:11.5px;color:var(--grey-text)}
.body-copy{left:31px;top:299px;width:526px;font-size:10.4px;line-height:13.35px;color:var(--body-text);text-align:justify;hyphens:auto}
.body-copy p{margin-bottom:13px}
.body-copy p.tight{margin-bottom:0}
.body-copy p.gap{margin-top:40px}
.signoff{right:41px;top:636px;font-size:15px;color:var(--grey-text)}
.signature{left:429px;top:671px;width:106px;height:67px;background:linear-gradient(90deg,#f1f1f1,#e6e6e6);border-radius:3px}
.footer{left:0;top:794px;width:588px;display:flex;align-items:center;gap:6px;font-size:11.5px}
.footer .rule{flex:1;border-top:1px solid var(--brand-blue)}

/* Business card front */
.card-front{left:711px;top:209px;width:411px;height:246px}
.card-front .wordmark{left:0;width:411px;top:63px;text-align:center;font-family:'Open Sans',sans-serif;font-weight:700;font-size:30px;color:var(--mark-grey)}
.person{right:221px;top:140px;text-align:right}
.person .name{font-size:15px;color:var(--name-blue);font-weight:500;letter-spacing:.3px;line-height:16px}
.person .title{font-family:'Open Sans',sans-serif;font-weight:600;font-size:8.5px;color:var(--grey-text);margin-top:2px}
.card-divider{left:199px;top:132px;height:46px;border-left:1px solid #d0d0d4}
.card-front .contact-list{left:206px;top:132px;font-size:10.5px;line-height:15.5px}
.band{left:0;top:200px;width:411px;height:20px;background:var(--brand-blue);color:#fff;font-size:10.5px;display:flex;align-items:center;justify-content:center}

/* Business card back */
.card-back{left:711px;top:498px;width:411px;height:247px;background:var(--brand-blue);display:flex;align-items:center;justify-content:center}
.card-back .wordmark{font-family:'Open Sans',sans-serif;font-weight:700;font-size:42px;color:#fff;letter-spacing:.5px}
</style>
</head>
<body>
<svg width="0" height="0" style="position:absolute">
  <defs>
    <symbol id="i-phone" viewBox="0 0 10 10"><path d="M2 1l2 0 .6 2-1 .9a5 5 0 0 0 2.5 2.5l.9-1 2 .6 0 2c0 .5-.4 1-1 1A8 8 0 0 1 1 2c0-.6.4-1 1-1z" fill="var(--icon)"/></symbol>
    <symbol id="i-mail" viewBox="0 0 10 10"><rect x="0.5" y="2" width="9" height="6" fill="var(--icon)"/><path d="M.5 2l4.5 3.5L9.5 2" fill="none" stroke="#fff" stroke-width=".8"/></symbol>
    <symbol id="i-web" viewBox="0 0 10 10"><g fill="none" stroke="var(--icon)" stroke-width=".9"><circle cx="5" cy="5" r="4.2"/><ellipse cx="5" cy="5" rx="1.8" ry="4.2"/><path d="M.8 5h8.4M1.6 3h6.8M1.6 7h6.8"/></g></symbol>
  </defs>
</svg>

<section class="sheet letter">
  <div class="abs wordmark">NORDVERK</div>
  <ul class="abs contact-list">
    <li><svg><use href="#i-phone"/></svg>(555) 014-2290</li>
    <li><svg><use href="#i-mail"/></svg>hello@nordverk.com</li>
    <li><svg><use href="#i-web"/></svg>www.nordverk.com</li>
  </ul>
  <div class="abs dash-rule"></div>

  <div class="abs recipient">
    <div class="name">Mr. Elias Berg</div>
    <div>(555) 014-2290</div>
    <div>hello@nordverk.com</div>
    <div class="addr">88 Harbor Row, Suite<br>40 Austin, TX 0000</div>
  </div>
  <div class="abs date">12 December, 2023</div>

  <div class="abs body-copy">
    <p>Lorem ipsum dolor sit amet, consectetuer adipiscing elit, sed diam nonummy nibh euismod tincidunt ut laoreet dolore magna aliquam erat volutpat. Ut wisi enim ad minim veniam, quis nostrud exerci tation ullamcorper suscipit lobortis nisl ut aliquip ex ea commodo consequat. Duis autem vel eum iriure dolor in hendrerit in vulputate velit esse molestie consequat, vel illum dolore eu feugiat nulla facilisis at vero eros et accumsan et iusto odio dignissim qui blandit praesent luptatum zzril delenit augue duis dolore te feugait nulla facilisi.</p>
    <p class="tight">Lorem ipsum dolor sit amet, cons ectetuer adipiscing elit, sed diam nonummy nibh euismod tincidunt ut laoreet dolore magna aliquam erat volutpat. Ut wisi enim ad minim veniam, quis nostrud exerci tation ullamcorper suscipit lobortis nisl ut aliquip ex ea commodo consequat.</p>
    <p>Lorem ipsum dolor sit amet, consectetuer adipiscing elit, sed diam nonummy nibh euismod tincidunt ut laoreet dolore magna aliquam erat</p>
    <p class="gap">Lorem ipsum dolor sit amet, cons ectetuer adipiscing elit, sed diam nonummy nibh euismod tincidunt ut laoreet dolore magna aliquam erat volutpat. Ut wisi enim ad minim veniam, quis nostrud exerci tation ullamcorper suscipit lobortis nisl ut aliquip ex ea commodo consequat. Lorem ipsum dolor sit zamet, consectetuer adipiscing elit, sed diam nonummy nibh euismod tincidunt.</p>
    <p>Lorem ipsum dolor sit amet, cons ectetuer adipiscing elit, sed diam nonummy nibh euismod tincidunt ut laoreet dolore magna aliquam erat volutpat. Ut wisi enim ad minim veniam, quis nostrud exerci tation ullamcorper suscipit lobortis nisl ut aliquip ex ea commodo consequat. Lorem ipsum dolor sit zamet, consectetuer adipiscing elit, sed diam nonummy nibh euismod tincidunt.</p>
  </div>

  <div class="abs signoff">Managing Director</div>
  <div class="abs signature" role="img" aria-label="Handwritten signature of the managing director"></div>

  <div class="abs footer">
    <span class="rule"></span>
    <span>88 Harbor Row, Suite 40, Austin, TX 0000</span>
    <span class="rule"></span>
  </div>
</section>

<section class="sheet card-front">
  <div class="abs wordmark">NORDVERK</div>
  <div class="abs person">
    <div class="name">ELIAS BERG</div>
    <div class="title">Director &nbsp;/ CEO</div>
  </div>
  <div class="abs card-divider"></div>
  <ul class="abs contact-list">
    <li><svg><use href="#i-phone"/></svg>(555) 014-2290</li>
    <li><svg><use href="#i-mail"/></svg>hello@nordverk.com</li>
    <li><svg><use href="#i-web"/></svg>www.nordverk.com</li>
  </ul>
  <div class="abs band">88 Harbor Row, Suite 40, Austin, TX 0000</div>
</section>

<section class="sheet card-back">
  <div class="wordmark">NORDVERK</div>
</section>
</body>
</html>
```